Firm of surveyors needs a professional yet friendly looking flyer

Our company offers help to landlords who have a phone mast on their property. We help them to negotiate the best rent and lease terms. There are so many landlords who don't seek professional advice because they don't know it's available. We want to send them a flyer which is informative, looks professional but also friendly so it prompts them to call us. I have attached the wording and some pictures but have more I can send but they were too large to attach.

Target Market(s)

Ranges from farmers to large corporations and land owners

Industry/Entity Type

Surveyor

Font styles to use
Sans Serif

Colors
acd136
9bcb3c
000000
ffffff
606060
848484

Requirements
Must have
• Must be clear, must give a professional look, must include pictures, must include our logo, must use our colour scheme (or variations of it). Ideally, I would like a try-fold design if possible.
Nice to have
• I would like there to be stand out lines to catch the readers eye (I have included some on the wording document). I would like a clean and modern design
Should not have
• Should not be too fussy

```html
<!DOCTYPE html>
<html lang="en">
<head>
<meta charset="utf-8">
<title>Relay Mast Group – Tri-fold Flyer</title>
<link rel="stylesheet" href="https://fonts.googleapis.com/css2?family=Open+Sans:wght@400;600;700&family=Raleway:wght@400;500&family=Roboto:wght@300;400&family=Roboto+Condensed:wght@300;400;700&display=swap">
<style>
:root{
  --backdrop:#8a6424;
  --blue:#3a6dbd;
  --blue-deep:#2f5fae;
  --blue-bright:#2f6fd0;
  --green:#4a7a30;
  --lime:#9bcb3c;
  --black:#000000;
  --white:#ffffff;
  --grey:#606060;
  --grey-light:#848484;
  --heading-green:#3f7a27;
}
*{margin:0;padding:0;box-sizing:border-box}
html,body{width:797px;height:1200px;overflow:hidden;background:var(--backdrop)}
body{position:relative;font-family:"Open Sans",sans-serif}
.sheet{position:absolute;left:56px;width:678px;height:528px;display:flex;box-shadow:3px 4px 8px rgba(0,0,0,.35)}
.sheet--outside{top:58px}
.sheet--inside{top:606px}
.panel{position:relative;width:226px;height:528px;overflow:hidden}

/* outside panels */
.services{background:var(--blue)}
.services__title{position:absolute;left:19px;top:20px;color:var(--white);font:700 21px/24px "Open Sans",sans-serif;letter-spacing:-.3px}
.services__list{position:absolute;left:18px;top:52px;list-style:none}
.services__list li{color:var(--white);font:300 11.6px/19.2px "Roboto",sans-serif;padding-left:15px;position:relative;white-space:nowrap}
.services__list li::before{content:"";position:absolute;left:0;top:6px;width:8px;height:8px;border-radius:50%;background:var(--lime)}
.services__photo{position:absolute;left:0;top:278px;width:226px;height:250px;background:linear-gradient(180deg,#3a6dbd 0%,#5d8fd6 60%,#a9c3e6 100%)}

.contact{background:var(--green)}
.contact__curve{position:absolute;inset:0}
.contact__name{position:absolute;left:17px;top:20px;color:var(--white);font:600 13px "Open Sans",sans-serif}
.contact__address{position:absolute;left:17px;top:42px;color:var(--white);font:400 9.4px/14px "Open Sans",sans-serif}
.contact__lines{position:absolute;left:16px;top:75px;list-style:none}
.contact__lines li{color:var(--white);font:400 9.2px/16.8px "Open Sans",sans-serif;display:flex;align-items:center;gap:6px}
.contact__lines li.web{font-weight:700}
.icon{width:13px;height:13px;border-radius:50%;background:var(--white);color:var(--green);font:700 8px/13px "Open Sans",sans-serif;text-align:center}
.cta{position:absolute;right:22px;top:168px;text-align:right;color:var(--white)}
.cta__head{font:700 21px/22px "Roboto Condensed",sans-serif}
.cta__sub{font:300 14.5px/16px "Roboto Condensed",sans-serif;margin-top:2px}
.cta__phone{position:absolute;left:0;width:226px;top:230px;text-align:center;color:var(--white);font:700 24px "Roboto Condensed",sans-serif;letter-spacing:.5px}
.bubble{position:absolute;left:44px;top:270px;width:146px;height:118px;display:flex;align-items:center;justify-content:center;text-align:center;color:var(--white);font:400 17px/26px "Open Sans",sans-serif}
.namebox{position:absolute;left:16px;top:432px;width:178px;height:84px;background:var(--white);border-radius:6px;box-shadow:0 0 6px rgba(0,0,0,.12);display:flex;align-items:center;justify-content:center;gap:7px}

.brand{display:flex;align-items:center;gap:7px;color:var(--heading-green);font:700 15px/17px "Open Sans",sans-serif;text-transform:uppercase}
.brand__dot{width:12px;height:12px;border-radius:50%;background:var(--heading-green);flex:none}

.cover{background:var(--white)}
.cover__photo{position:absolute;left:0;top:130px;width:226px;height:320px;background:linear-gradient(180deg,#ffffff 0%,#cfe0f1 30%,#b6cfe8 55%,#7ea354 72%,#5d8a3a 100%)}
.cover__brand{position:absolute;left:26px;top:48px}
.cover__tag{position:absolute;left:0;width:226px;top:120px;text-align:center;color:#222;font:300 16.5px/20px "Roboto",sans-serif}
.cover__band{position:absolute;inset:0}
.cover__note{position:absolute;left:10px;width:206px;top:446px;text-align:center;color:var(--white);font:300 12.4px/17.6px "Roboto",sans-serif}

/* inside panels */
.copy{background:var(--white);color:var(--grey);font:400 7.3px/10.7px "Raleway",sans-serif;text-align:justify}
.copy__body{position:absolute;left:17px;right:17px;top:26px}
.copy__body p{margin-bottom:9px}
.copy__body h2{color:var(--heading-green);font:700 12px/15px "Open Sans",sans-serif;text-align:left;margin:0 0 7px;white-space:nowrap}
.copy__body h2.gap{margin-top:6px}

.offer{background:var(--blue-deep);color:var(--white)}
.offer__top{position:absolute;left:12px;right:22px;top:26px;font:400 7.2px/10.2px "Raleway",sans-serif;text-align:justify}
.offer__top p{margin-bottom:10px}
.offer__top p.small{font-size:6.4px;line-height:10px;opacity:.95}
.offer__rule{position:absolute;left:12px;right:22px;top:141px;height:1px;background:rgba(255,255,255,.75)}
.offer__lower{position:absolute;left:0;top:152px;width:226px;height:322px;background:var(--blue-bright)}
.offer__photo{position:absolute;left:157px;top:226px;width:69px;height:248px;background:linear-gradient(180deg,#e6ecf2 0%,#c9d3dd 60%,#9fb0c2 100%)}
.offer__head{position:absolute;left:12px;top:162px;font:700 22.5px/30px "Open Sans",sans-serif;white-space:nowrap}
.offer__q{position:absolute;left:12px;top:236px;font:400 15.5px/19px "Open Sans",sans-serif}
.offer__help{position:absolute;left:12px;top:294px;font:400 14.5px/19px "Open Sans",sans-serif}
.offer__help .big{font:700 19px/25px "Open Sans",sans-serif}
.offer__help .mid{font:400 19px/29px "Open Sans",sans-serif}
.offer__excl{position:absolute;left:12px;top:426px;font:300 12px/15.2px "Roboto",sans-serif}

.footer{position:absolute;left:0;top:474px;width:226px;height:54px;background:var(--green);color:var(--white)}
.footer--call{text-align:right;padding:2px 22px 0 0}
.footer--call .cta__head{font-size:20px;line-height:26px;margin-top:6px}
.footer--call .cta__sub{font-size:12.4px;line-height:14px;margin-top:0}
.footer--phone{display:flex;align-items:center;justify-content:center;font:700 28px "Roboto Condensed",sans-serif;letter-spacing:.5px}
.footer--web{display:flex;align-items:center;padding-left:12px;font:700 12px "Open Sans",sans-serif}
.divider{border-left:1px solid rgba(0,0,0,.12)}
</style>
</head>
<body>

<section class="sheet sheet--outside">
  <div class="panel services">
    <h2 class="services__title">OUR SERVICES</h2>
    <ul class="services__list">
      <li>Rent Reviews</li>
      <li>Lease Renewals</li>
      <li>Network Consolidation Issues</li>
      <li>Site Shares</li>
      <li>Rent Protection</li>
      <li>Equipment Upgrades</li>
      <li>Mast Removals / Decommissioning</li>
      <li>Mast Sales and Marketing</li>
      <li>Land Marketing for Masts</li>
      <li>Mast Management and Portfolios</li>
      <li>Safety Testing</li>
    </ul>
    <div class="services__photo" role="img" aria-label="Photo of a lattice telecoms mast with antennas against a blue sky"></div>
  </div>

  <div class="panel contact">
    <svg class="contact__curve" width="226" height="528" viewBox="0 0 226 528">
      <path d="M0,318 C70,350 150,390 226,410 L226,528 L0,528 Z" fill="#f8f8f5"/>
      <path d="M40,320 C100,360 170,385 226,395 L226,412 C160,400 95,375 40,320 Z" fill="#000"/>
      <circle cx="114" cy="329" r="72" fill="var(--lime)"/>
      <circle cx="118" cy="329" r="69" fill="#111"/>
    </svg>
    <h1 class="contact__name">Relay Mast Group Ltd</h1>
    <p class="contact__address">Unit 4 Beacon Court, Harbour Business Park,<br>Oakfield, Westshire, WS4 2QT.</p>
    <ul class="contact__lines">
      <li><span class="icon">t</span>01632 960418</li>
      <li><span class="icon">f</span>01632 960419</li>
      <li><span class="icon">e</span>info@relaymastgroup.co.uk</li>
      <li class="web"><span class="icon">w</span>www.relaymastgroup.co.uk</li>
    </ul>
    <div class="cta">
      <div class="cta__head">CALL US NOW</div>
      <div class="cta__sub">FOR A FREE, NO<br>OBLIGATION CHAT</div>
    </div>
    <div class="cta__phone">01632 960418</div>
    <div class="bubble">Unsure<br>whether you<br>are getting the<br>best rent?</div>
    <div class="namebox"><span class="brand"><span class="brand__dot"></span>Relay Mast<br>Group</span></div>
  </div>

  <div class="panel cover">
    <div class="cover__photo" role="img" aria-label="Photo of a telecoms mast on a grassy hillside under a pale sky"></div>
    <svg class="cover__band" width="226" height="528" viewBox="0 0 226 528">
      <path d="M0,412 C80,430 170,425 226,380 L226,528 L0,528 Z" fill="var(--green)"/>
      <path d="M0,395 C90,420 170,410 226,372 L226,385 C170,425 80,432 0,412 Z" fill="#000"/>
    </svg>
    <div class="cover__brand"><span class="brand" style="font-size:19px;line-height:22px"><span class="brand__dot" style="width:16px;height:16px"></span>Relay Mast<br>Group</span></div>
    <p class="cover__tag">We act EXCLUSIVELY for<br>landlords on ALL phone<br>mast matters</p>
    <p class="cover__note">Our expert surveyors will be happy to help you understand proposed changes and what they could mean for you</p>
  </div>
</section>

<section class="sheet sheet--inside">
  <div class="panel copy">
    <div class="copy__body">
      <p>Relay Mast Group is a firm of telecoms surveyors with over 15 years' experience of dealing with mobile phone mast operators. We have built up a massive database of thousands of comparable mobile phone mast deals to aid us in our telecoms negotiations. All our surveyors have spent time working for phone mast operators and know the industry inside out. We now work exclusively for landlords, fighting your corner, ensuring our landlords get the highest rents and best lease terms available in the market place.</p>
      <p>Many of the original mobile phone mast leases / agreements are now coming up for renewal. This is an ideal opportunity for landlords to achieve the best deal. We are currently offering to review telecoms leases for free and provide landlords with our recommendations. If you would like to take us up on this free no obligation offer, send a copy of your agreement and any recent correspondence to us, either via post or email using the details on this flyer. Please also provide us with your name, contact number and let us know the current rent you are achieving so we can see if there is room for improvement. Once we have received this, one of our surveyors will give you a call when convenient to talk through your lease with you, highlighting anything we feel needs addressing, any opportunity to increase the rent, or to discuss a specific issue you are having with your mast (i.e. an upgrade request).</p>
      <p>Recently, operators have been attempting to cut costs by reducing rents. They are joining forces in an effort to drive rents down. Many landlords are contacting us after receiving a letter from the operators / operator's agent, telling them they must accept a rent reduction or risk losing their site. In the majority of cases, Relay Mast Group can prevent this from occurring and protect the landlord's rental income.</p>
    </div>
    <div class="footer footer--call">
      <div class="cta__head">CALL US NOW</div>
      <div class="cta__sub">FOR A FREE, NO OBLIGATION CHAT</div>
    </div>
  </div>

  <div class="panel copy divider">
    <div class="copy__body">
      <h2>Sell Your Phone Mast</h2>
      <p>We can also assist landlords in selling their phone mast. We have strong links with many large investors who regularly purchase the freehold or leasehold interest of masts and will pay a cash lump sum, often, even hundreds of thousands of pounds. This can be done in a matter of weeks and the cash is yours to spend however you like, regardless of whether the mast stays for the duration of the investors leasehold or not. We can negotiate flexible terms, such as a buyback option so please call us today to discuss.</p>
      <h2 class="gap">Getting A Phone Mast</h2>
      <p>If you don't currently have a mast located on your land but are interested in receiving thousands of pounds a year in rental income, or you have a redundant mast you would like to market, we offer a free advertising service on our website. We will market your land to phone mast operators with a view to having a mast located there. Please visit the 'Advertise My Site' link on our website to take advantage of this service.</p>
      <h2 class="gap">The Current Telecoms Climate</h2>
      <p>The telecoms market, in relation to mobile phone masts, is going through some huge changes. Operators are combining to cut costs. We have already seen Northcell join forces with Skyline and Brightlink to form a jointly owned company with Arcwave called Tower Share Ltd. More recently, Skyline and Brightlink have merged to form Unity Networks Ltd to become the new network leader. What this can mean for the landlord is changes to their site and potentially the loss of income. It can all be very confusing but don't worry, this is where we can help. We know the telecoms industry and understand how a new situation may affect a landlord, therefore,</p>
    </div>
    <div class="footer footer--phone">01632 960418</div>
  </div>

  <div class="panel offer">
    <div class="offer__top">
      <p>allowing us to provide the best advice on protecting your asset.</p>
      <p class="small">In April 2017 the Government introduced the Digital Economy Act. This sets out significant changes for landlords including the way rents are calculated. We have already seen operators contact landlords trying to reduce their rent in light of this new law. We are working alongside specialist telecoms solicitors to try to reduce the potential negative impact on landlords.</p>
    </div>
    <div class="offer__rule"></div>
    <div class="offer__lower"></div>
    <div class="offer__photo" role="img" aria-label="Photo of a white telecoms antenna pole with panel antennas and dishes"></div>
    <h2 class="offer__head">Interested in<br>selling your site?</h2>
    <p class="offer__q">Or already have<br>an offer?</p>
    <p class="offer__help"><span class="big">We can help</span><br><span class="big">you</span> to achieve<br>the best sale price,<br><span class="mid">quickly</span></p>
    <p class="offer__excl">We act EXCLUSIVELY<br>for landlords on ALL<br>phone mast matters</p>
    <div class="footer footer--web">www.relaymastgroup.co.uk</div>
  </div>
</section>

</body>
</html>
```